Brindle's Business Card

I need some designs for a new business card including the new logo attached. An old example of our business card is also attached to show all the data that should be included on the new design.
**I added some more examples someone had mocked up**

Contact Information for Business Card

Should include all info on other examples uploaded.

```html
<!DOCTYPE html>
<html lang="en">
<head>
<meta charset="utf-8">
<title>Brindle's Business Card</title>
<link href="https://fonts.googleapis.com/css2?family=Montserrat:wght@400;500;600&family=Oswald:wght@500;600&display=swap" rel="stylesheet">
<style>
  :root {
    --backdrop: #3b3b3d;
    --paper: #ffffff;
    --brand-blue: #0b6bb5;
    --brand-red: #e4222b;
    --ink: #2b2b2b;
    --soft-blue: #e8f1fa;
  }
  html, body {
    margin: 0;
    width: 1200px;
    height: 1200px;
    overflow: hidden;
    background: var(--backdrop);
  }
  .stage {
    position: relative;
    width: 1200px;
    height: 1200px;
  }
  .card {
    position: absolute;
    left: 250px;
    width: 700px;
    height: 400px;
    border-radius: 28px;
    overflow: hidden;
    box-shadow: 0 18px 40px rgba(0,0,0,.35);
  }
  /* Contact side */
  .card--contact {
    top: 150px;
    background: var(--paper);
  }
  .contact__mark {
    position: absolute;
    right: -60px;
    top: -40px;
    width: 380px;
    height: 380px;
    border-radius: 50%;
    background: var(--soft-blue);
  }
  .contact__body {
    position: absolute;
    left: 56px;
    top: 96px;
  }
  .contact__name {
    font-family: "Montserrat", sans-serif;
    font-weight: 600;
    font-size: 36px;
    letter-spacing: 1px;
    color: var(--brand-blue);
    margin: 0 0 18px;
  }
  .contact__list {
    list-style: none;
    margin: 0;
    padding: 0;
  }
  .contact__item {
    display: flex;
    align-items: center;
    gap: 14px;
    font-family: "Montserrat", sans-serif;
    font-weight: 400;
    font-size: 22px;
    color: var(--ink);
    margin-bottom: 8px;
  }
  .contact__icon {
    width: 24px;
    height: 24px;
    flex: none;
  }
  .contact__claims {
    margin-top: 26px;
    font-family: "Oswald", sans-serif;
    font-weight: 600;
    font-size: 28px;
    line-height: 1.15;
    text-transform: uppercase;
  }
  .claim--licensed { color: var(--brand-blue); }
  .claim--family { color: var(--brand-red); }

  /* Brand side */
  .card--brand {
    top: 640px;
    background: var(--brand-blue);
  }
  .brand__lockup {
    position: absolute;
    left: 60px;
    top: 110px;
    display: flex;
    align-items: center;
    gap: 26px;
  }
  .brand__dot {
    width: 110px;
    height: 110px;
    border-radius: 50%;
    background: var(--paper);
    flex: none;
  }
  .brand__name {
    font-family: "Montserrat", sans-serif;
    font-weight: 600;
    font-size: 84px;
    line-height: 1;
    color: var(--paper);
    margin: 0;
    letter-spacing: 1px;
  }
  .brand__service {
    font-family: "Montserrat", sans-serif;
    font-weight: 500;
    font-size: 19px;
    letter-spacing: 1.5px;
    color: var(--brand-red);
    text-transform: uppercase;
    margin-top: 8px;
  }
  .brand__area {
    position: absolute;
    left: 0;
    right: 0;
    bottom: 46px;
    text-align: center;
    font-family: "Oswald", sans-serif;
    font-weight: 500;
    font-size: 30px;
    color: var(--paper);
    text-transform: uppercase;
    letter-spacing: .5px;
  }
</style>
</head>
<body>
<main class="stage">
  <section class="card card--contact">
    <div class="contact__mark"></div>
    <div class="contact__body">
      <h1 class="contact__name">DYLAN BRINDLE</h1>
      <ul class="contact__list">
        <li class="contact__item">
          <svg class="contact__icon" viewBox="0 0 24 24"><path fill="#0b6bb5" d="M6.6 10.8a15.1 15.1 0 0 0 6.6 6.6l2.2-2.2a1 1 0 0 1 1-.25 11.4 11.4 0 0 0 3.6.57 1 1 0 0 1 1 1V20a1 1 0 0 1-1 1A17 17 0 0 1 3 4a1 1 0 0 1 1-1h3.5a1 1 0 0 1 1 1c0 1.25.2 2.45.57 3.57a1 1 0 0 1-.25 1z"/></svg>
          555.014.2287
        </li>
        <li class="contact__item">
          <svg class="contact__icon" viewBox="0 0 24 24"><rect x="2" y="5" width="20" height="14" rx="1" fill="#0b6bb5"/><path d="M2.5 6 12 13l9.5-7" fill="none" stroke="#fff" stroke-width="1.6"/></svg>
          hvacbrindle@mailbox.net
        </li>
        <li class="contact__item">
          <svg class="contact__icon" viewBox="0 0 24 24" fill="none" stroke="#0b6bb5" stroke-width="1.8"><circle cx="12" cy="12" r="10"/><ellipse cx="12" cy="12" rx="4.5" ry="10"/><path d="M2 12h20M4 7h16M4 17h16"/></svg>
          www.yourwebsite.com
        </li>
      </ul>
      <div class="contact__claims">
        <div class="claim--licensed">Licensed &amp; Insured</div>
        <div class="claim--family">Family Owned &amp; Operated</div>
      </div>
    </div>
  </section>

  <section class="card card--brand">
    <div class="brand__lockup">
      <div class="brand__dot"></div>
      <div>
        <h2 class="brand__name">BRINDLE'S</h2>
        <div class="brand__service">Air Conditioning &amp; Heating Service</div>
      </div>
    </div>
    <div class="brand__area">Serves Maple Ridge, IA &amp; Surrounding Areas</div>
  </section>
</main>
</body>
</html>
```